Etiketten-Design für Kaffeetüten
Zielgruppe
Wir stellen eine nachhaltige alternative zu herkömmlichem Bohnenkaffee her.
Regional, nachhaltig und koffeinfrei.
Hierzu verwenden wir Süßlupinen die wir von einem Partnerbauern aus Niedersachsen beziehen. Diese Lupinen werden wie herkömmlicher Kaffee in einem Trommelröster geröstet und anschließend gemahlen.
Unser Lupinenkaffee kann wie herkömmlicher Kaffee im Filter in der Frenchpress oder in einem Espressokocher zubereitet werden.
Wir bieten unseren Kunden zwei verschiedene Sorten an, eine 'Mild' und eine 'Klassisch'.
Die Zielgruppe sind ernährungsbewusste Menschen die gezielt eine alternative zu herkömmlichen Bohnenkaffee suchen. (Koffeinfreier Kaffee, Getreidekaffee)
Aufgabenstellung
Wir möchten ein modernes Design des Etiketts, das den Stil des Logos widerspiegelt. Die beiden Sorten 'Mild' und 'Klassisch' sollten gut von einander zu unterscheiden sein.
Es gibt ein Etikett für die Vorderseite, hier soll die Produktbezeichnung 'Lupinenkaffee' sowie die Mengenangabe '500g' stehen.
Ggf. 3 Icons für mögliche Brühmethoden (Filter, Frenchpress, Espressokocher)
Auf dem Etikett der Rückseite müssen zum einen die Zutaten, die Zubereitung sowie die Nährwertangaben (in TabellenForm) angegeben werden. Sowie ein EAN Code die Herstellerangaben und die Adresse der Homepage.
FENNO BREW – Deine nachhaltige Kaffeealternative
Zutaten: weiße Süßlupinen, geröstet
Zubereitung: Du kannst Deinen Lupinenkaffee mit der French Press, dem klassischen Filter oder dem Espressokocher zubereiten. Für den optimalen Geschmack empfehlen wir 8g Kaffeepulver für 100ml.
Hersteller:
FENNO GmbH
Birkenhainer Weg 57
40213 Düsseldorf
www.FENNOBREW.de
 Nährwertangaben für 100 ml Kaffee
Energie 12kj - 5 kcal
Fett <0,1g
Davon gesättigt <0,1g
Kohlenhydrate <1,0g
Davon Zucker <0,05g
Eiweiß <1,0g
Salz <0,05g
Die Kaffeetüte, auf die das Etikett geklebt wird, ist in einer braunen Kartonfarbe.
Das Etikett für die Kaffeetüten hat die Maße 7x11.
Das Logo hat die Schriftart 'Cera'. Die verwendete Schriftart sollte möglichst gleich sein, oder gut damit harmonieren.

```html
<!DOCTYPE html>
<html lang="de">
<head>
<meta charset="utf-8">
<title>FENNO BREW – Lupinenkaffee Etiketten</title>
<link href="https://fonts.googleapis.com/css2?family=Jost:wght@400;500;600&display=swap" rel="stylesheet">
<style>
  :root {
    --board: #e6e6e6;
    --paper: #ffffff;
    --ink: #1b1b1b;
    --classic: #ee7550;
    --mild: #86bdb2;
    --pattern: #3a3a3a;
  }
  * { box-sizing: border-box; margin: 0; padding: 0; }
  html, body { width: 1200px; height: 1200px; overflow: hidden; }
  body {
    background: var(--board);
    font-family: 'Jost', 'Helvetica Neue', Arial, sans-serif;
    color: var(--ink);
    position: relative;
  }
  .label {
    position: absolute;
    width: 316px;
    background: var(--paper);
    box-shadow: 0 2px 8px rgba(0,0,0,0.18);
    overflow: hidden;
  }
  .label--front { height: 499px; top: 91px; }
  .label--back { height: 468px; top: 638px; }
  .label--left { left: 216px; }
  .label--right { left: 631px; }
  .label--classic { --accent: var(--classic); }
  .label--mild { --accent: var(--mild); }

  .center { position: absolute; left: 0; right: 0; text-align: center; }

  /* front */
  .brand-mark {
    position: absolute; left: 118px; top: 31px;
    width: 80px; height: 80px; border: 2px solid var(--ink); border-radius: 50%;
  }
  .brand-name { top: 122px; font-size: 17px; font-weight: 500; letter-spacing: 0.18em; }
  .rule { position: absolute; left: 46px; width: 224px; height: 1.5px; background: var(--ink); }
  .product-name {
    top: 184px; font-size: 36px; font-weight: 400; letter-spacing: 0.32em;
    line-height: 46px; padding-left: 0.32em;
  }
  .variety-tag {
    position: absolute; top: 290px; left: 50%; transform: translateX(-50%);
    background: var(--accent); border: 1.5px solid var(--ink);
    padding: 2px 10px 1px; font-size: 17px; letter-spacing: 0.12em; font-weight: 500;
    white-space: nowrap;
  }
  .brew-icons {
    position: absolute; top: 340px; left: 0; right: 0;
    display: flex; justify-content: center; gap: 18px;
  }
  .brew-icons svg { width: 28px; height: 34px; fill: var(--ink); }
  .pattern-band {
    position: absolute; left: 0; right: 0; top: 395px; bottom: 0;
    background: linear-gradient(180deg, #6a6a6a, var(--pattern));
  }
  .weight-badge {
    position: absolute; left: 230px; top: 395px; width: 72px; height: 72px;
    border-radius: 50%; background: var(--ink); color: var(--paper);
    display: flex; align-items: center; justify-content: center;
    font-size: 18px; font-weight: 500; letter-spacing: 0.05em;
    border: 3px solid var(--paper);
  }

  /* back */
  .back-title { top: 24px; font-size: 23px; font-weight: 600; letter-spacing: 0.22em; padding-left: 0.22em; }
  .claims { top: 63px; display: flex; flex-direction: column; align-items: center; gap: 3px; }
  .claims span {
    background: var(--accent); color: var(--paper);
    font-size: 11.5px; padding: 1px 4px; line-height: 15px;
  }
  .section-tag {
    position: absolute; top: 118px; left: 50%; transform: translateX(-50%);
    border: 1px solid var(--ink); padding: 2px 7px; font-size: 10.5px; letter-spacing: 0.04em;
  }
  .preparation { top: 148px; padding: 0 22px; font-size: 10.4px; line-height: 14.5px; }
  .ingredients { top: 237px; font-size: 10px; letter-spacing: 0.02em; }
  .ingredients strong { font-weight: 600; }
  .nutrition { position: absolute; left: 52px; top: 264px; width: 125px; font-size: 9px; }
  .nutrition caption {
    background: var(--ink); color: var(--paper); text-align: left;
    font-size: 9px; line-height: 12px; padding: 3px 5px; letter-spacing: 0.03em;
  }
  .nutrition table { width: 100%; border-collapse: collapse; margin-top: 10px; }
  .nutrition td { line-height: 11.2px; padding: 0; }
  .nutrition td:last-child { text-align: right; }
  .nutrition .sub { padding-left: 7px; }
  .maker { top: 386px; font-size: 10px; line-height: 14px; letter-spacing: 0.02em; }
  .web-bar {
    position: absolute; top: 422px; left: 70px; width: 182px; height: 21px;
    background: var(--ink); color: var(--paper); text-align: center;
    font-size: 12.5px; line-height: 21px; font-weight: 500; letter-spacing: 0.12em;
  }
</style>
</head>
<body>

<svg width="0" height="0" style="position:absolute" aria-hidden="true">
  <defs>
    <symbol id="icon-moka" viewBox="0 0 28 34">
      <rect x="11" y="1" width="6" height="3"/>
      <path d="M6 5h16l-3 11H9z"/>
      <path d="M8 17h12l3 15H5z"/>
      <path d="M22 8h4v2h-3z"/>
    </symbol>
    <symbol id="icon-press" viewBox="0 0 28 34">
      <rect x="13" y="0" width="2" height="6"/>
      <rect x="9" y="5" width="10" height="2"/>
      <rect x="6" y="7" width="15" height="24"/>
      <path d="M21 11h5v14h-5v-2h3V13h-3z"/>
      <rect x="5" y="31" width="17" height="2"/>
    </symbol>
    <symbol id="icon-pour" viewBox="0 0 28 34">
      <path d="M3 3h22l-8 12h-6z"/>
      <rect x="6" y="15" width="16" height="2"/>
      <path d="M6 18h16v14H6z" fill="none" stroke="#1b1b1b" stroke-width="2"/>
      <path d="M6 24h16v8H6z"/>
    </symbol>
  </defs>
</svg>

<!-- Front, Klassisch -->
<section class="label label--front label--left label--classic">
  <div class="brand-mark"></div>
  <div class="center brand-name">FENNO BREW</div>
  <div class="rule" style="top:174px"></div>
  <h1 class="center product-name">LUPINEN<br>KAFFEE</h1>
  <div class="variety-tag">KLASSISCH</div>
  <div class="brew-icons">
    <svg><use href="#icon-moka"/></svg>
    <svg><use href="#icon-press"/></svg>
    <svg><use href="#icon-pour"/></svg>
  </div>
  <div class="pattern-band" role="img" aria-label="Schwarz-weißes Muster aus gezackten Wellenlinien"></div>
  <div class="weight-badge">500G</div>
</section>

<!-- Front, Mild -->
<section class="label label--front label--right label--mild">
  <div class="brand-mark"></div>
  <div class="center brand-name">FENNO BREW</div>
  <div class="rule" style="top:174px"></div>
  <h1 class="center product-name">LUPINEN<br>KAFFEE</h1>
  <div class="variety-tag">MILD</div>
  <div class="brew-icons">
    <svg><use href="#icon-moka"/></svg>
    <svg><use href="#icon-press"/></svg>
    <svg><use href="#icon-pour"/></svg>
  </div>
  <div class="pattern-band" role="img" aria-label="Schwarz-weißes Muster aus verstreuten Dreiecken"></div>
  <div class="weight-badge">500G</div>
</section>

<!-- Back, Klassisch -->
<section class="label label--back label--left label--classic">
  <h2 class="center back-title">FENNO BREW</h2>
  <div class="center claims">
    <span>Deine regionale Kaffeealternative</span>
    <span>koffeinfrei - magenfreundlich - nachhaltig</span>
  </div>
  <div class="section-tag">ZUBEREITUNG</div>
  <p class="center preparation">Du kannst Deinen Lupinenkaffee mit der French Press, dem klassischen Filter oder dem Espresso-kocher zubereiten. Für den optimalen Geschmack empfehlen wir 8g Kaffeepulver für 100ml Wasser.</p>
  <div class="rule" style="top:222px; left:22px; width:272px"></div>
  <p class="center ingredients">ZUTATEN: weiße <strong>Süßlupinen</strong>, geröstet</p>
  <div class="nutrition">
    <table>
      <caption>NÄHRWERTANGABEN<br>FÜR 100 ML KAFFEE</caption>
      <tr><td>Energie</td><td>12 kj - 5 kcal</td></tr>
      <tr><td>Fett</td><td>&lt; 0,1 g</td></tr>
      <tr><td class="sub">Davon gesättigt</td><td>&lt; 0,1 g</td></tr>
      <tr><td>Kohlenhydrate</td><td>&lt; 1,0 g</td></tr>
      <tr><td class="sub">Davon Zucker</td><td>&lt; 0,5 g</td></tr>
      <tr><td>Eiweiß</td><td>&lt; 1,0 g</td></tr>
      <tr><td>Salz</td><td>&lt; 0,05 g</td></tr>
    </table>
  </div>
  <p class="center maker">HERSTELLER: FENNO GmbH<br>Birkenhainer Weg 57 - 40213 Düsseldorf</p>
  <div class="web-bar">www.FENNOBREW.de</div>
</section>

<!-- Back, Mild -->
<section class="label label--back label--right label--mild">
  <h2 class="center back-title">FENNO BREW</h2>
  <div class="center claims">
    <span>Deine regionale Kaffeealternative</span>
    <span>koffeinfrei - magenfreundlich - nachhaltig</span>
  </div>
  <div class="section-tag">ZUBEREITUNG</div>
  <p class="center preparation">Du kannst Deinen Lupinenkaffee mit der French Press, dem klassischen Filter oder dem Espresso-kocher zubereiten. Für den optimalen Geschmack empfehlen wir 8g Kaffeepulver für 100ml Wasser.</p>
  <div class="rule" style="top:222px; left:22px; width:272px"></div>
  <p class="center ingredients">ZUTATEN: weiße <strong>Süßlupinen</strong>, geröstet</p>
  <div class="nutrition">
    <table>
      <caption>NÄHRWERTANGABEN<br>FÜR 100 ML KAFFEE</caption>
      <tr><td>Energie</td><td>12 kj - 5 kcal</td></tr>
      <tr><td>Fett</td><td>&lt; 0,1 g</td></tr>
      <tr><td class="sub">Davon gesättigt</td><td>&lt; 0,1 g</td></tr>
      <tr><td>Kohlenhydrate</td><td>&lt; 1,0 g</td></tr>
      <tr><td class="sub">Davon Zucker</td><td>&lt; 0,5 g</td></tr>
      <tr><td>Eiweiß</td><td>&lt; 1,0 g</td></tr>
      <tr><td>Salz</td><td>&lt; 0,05 g</td></tr>
    </table>
  </div>
  <p class="center maker">HERSTELLER: FENNO GmbH<br>Birkenhainer Weg 57 - 40213 Düsseldorf</p>
  <div class="web-bar">www.FENNOBREW.de</div>
</section>

</body>
</html>
```